Forestry Industry Connection Website

We are requiring a template design that users of this system can feel comfortable with, we have attached some basic layout ideas, to point you guys in the right direction, but we need the graphic concept taken to a much higher professional level.
TimberLinkup.net plans to connect professionals and employers in the industry worldwide, we would like a design that is very easy to navigate, and reflects the green/natural/environmental nature of the industry.
We will need-
1 - A home page
2 - a dashboard page
3 - a profile page
4 - a display projects, list and details pages
5 - Most of our main menus will have sub headings, so we'll need a drop down menu design.
6 - a forum layout design
7 - chatterbook and chirpnet icons integrated throughout
The logo supplied on the example designs is our final logo, so we would like the site design to complement it.
We would need the final approved designed to be coded in HTML5/CSS along with the PSD files.
UPDATE-
We have uploaded a new PDF file with a revised layout concept for the homepage, the idea keeping the most important information right at the top of the page.
also uploaded is the timber linkkup logo in EPS format and some JPEG's of forest plantation.
Looking forward to seeing your design concepts.
Updates
we've added a PDF file with an idea of menus, and where info should be on the page, keeping most of the important information right at the top of the page. We have also added the TimberLinukp Logo in EPS format.

```html
<!DOCTYPE html>
<html lang="en">
<head>
<meta charset="utf-8">
<title>TimberLinkup.net – Home</title>
<link href="https://fonts.googleapis.com/css2?family=Open+Sans:ital,wght@0,400;0,600;0,700;1,700&family=PT+Sans:wght@400;700&family=Uncial+Antiqua&display=swap" rel="stylesheet">
<style>
:root{
  --forest-dark:#123a1c;
  --forest-teal:#1e5a4c;
  --green:#2f9a16;
  --green-deep:#1c7a0c;
  --green-text:#2a7d12;
  --panel-green:#2b4424;
  --panel-border:#8fa38a;
  --tab-blue:#2b8fcf;
  --tab-blue-dark:#1565a0;
  --row-teal:#a7c9bb;
  --row-pale:#e9f5e4;
  --text:#222;
  --white:#fff;
}
*{box-sizing:border-box;margin:0;padding:0}
html,body{width:755px;height:1200px;overflow:hidden;background:var(--white)}
body{position:relative;font-family:"Open Sans",Arial,sans-serif;color:var(--text)}
.abs{position:absolute}

/* header */
.site-header{left:0;top:0;width:755px;height:119px;
  background:linear-gradient(180deg,var(--forest-dark) 0,var(--forest-teal) 22px,#6f9c92 45px,#d9e7e4 70px,#fff 95px)}
.util-bar{right:28px;top:10px;display:flex;align-items:center;gap:10px;font:700 9px "Open Sans",sans-serif;color:var(--white)}
.util-bar select{width:66px;height:14px;font-size:8px;border:1px solid #888;background:#eee}
.util-bar .sep{opacity:.8}
.brand{left:18px;top:66px;display:flex;align-items:center;gap:6px}
.brand-dot{width:28px;height:28px;border-radius:50%;background:var(--green-deep)}
.brand-name{font:700 20px "PT Sans",sans-serif;color:var(--forest-dark)}

.hero{left:0;top:119px;width:755px;height:130px;
  background:linear-gradient(180deg,#8fb25a 0,#5d8a3a 40%,#3f6a2a 75%,#2a4a1e 100%);border-top:1px solid #333}
.hero-title{left:18px;top:198px;font:400 28px/34px "Uncial Antiqua",serif;color:var(--white);text-shadow:1px 1px 3px #000;white-space:nowrap}

.main-nav{left:0;top:249px;width:755px;height:28px;background:linear-gradient(180deg,#3fb322,var(--green-deep));display:flex;padding-left:14px}
.main-nav a{color:var(--white);text-decoration:none;font:400 13px "PT Sans",sans-serif;padding:6px 10px;border-right:1px solid #5cc33d;border-left:1px solid #1a6c0a}

/* body frame */
.frame{left:13px;top:287px;width:729px;height:900px;border-radius:14px;background:linear-gradient(180deg,#ececec,#f6f6f6 40%,#fff);border:1px solid #ccc}

.featured{left:24px;top:298px;width:708px;height:69px;border-radius:10px;background:linear-gradient(#efefef,#d3d3d3);border:1px solid #bbb;box-shadow:0 3px 0 #aaa}
.featured h2{position:absolute;left:14px;top:10px;font:400 14px "PT Sans",sans-serif;color:#222}
.partner-badges{position:absolute;left:165px;top:14px;display:flex;gap:26px;align-items:center}
.badge{width:40px;height:40px;background:#8f8f8f;border-radius:4px;opacity:.75}
.badge.wide{width:110px;height:26px}

.how-it-works{left:24px;top:377px;width:708px;height:142px;border-radius:10px;background:var(--panel-green);border:2px solid var(--panel-border)}
.how-it-works h2{position:absolute;left:12px;top:6px;font:400 14px "PT Sans",sans-serif;color:var(--white)}
.steps{position:absolute;left:12px;top:22px;width:680px;display:flex}
.step{flex:1;height:110px;position:relative;border-right:1px solid #3c5934}
.step:last-child{border:none}
.step-art{position:absolute;left:50%;top:14px;width:62px;height:62px;margin-left:-31px;border-radius:10px}
.step-label{position:absolute;left:50%;top:88px;transform:translateX(-50%);background:linear-gradient(#2c7a1a,#1a4f10);color:var(--white);font:400 12px "PT Sans",sans-serif;padding:2px 12px 2px 10px;white-space:nowrap;clip-path:polygon(0 0,90% 0,100% 50%,90% 100%,0 100%)}

.card{border-radius:10px;background:var(--white);border:2px solid #d6d6d6}
.tab{position:absolute;left:-4px;top:12px;height:28px;padding:0 28px 0 10px;display:flex;align-items:center;gap:6px;
  background:linear-gradient(#5fb4e6,var(--tab-blue) 55%,var(--tab-blue-dark));color:var(--white);font:400 14px "PT Sans",sans-serif;
  clip-path:polygon(0 0,92% 0,100% 50%,92% 100%,0 100%)}
.tab svg{width:11px;height:11px}

.signup{left:22px;top:528px;width:347px;height:266px}
.signup h3{position:absolute;left:10px;font:italic 700 10px "Open Sans",sans-serif;color:var(--green-text)}
.signup ul{position:absolute;left:14px;list-style:none}
.signup li{font-size:8.5px;color:var(--green-text);line-height:15px;padding-left:18px;position:relative}
.signup li::before{content:"";position:absolute;left:2px;top:3px;width:6px;height:5px;border-left:1px solid #666;border-bottom:1px solid #666}

.testimonial{left:385px;top:528px;width:347px;height:266px}
.testimonial .quote{position:absolute;left:8px;top:52px;width:330px;font-size:8px;line-height:12px;color:#222}
.testimonial .quote p{margin-bottom:12px}
.byline{position:absolute;left:8px;top:206px;font:italic 700 9.5px "Open Sans",sans-serif;color:var(--green-text)}
.more-link{font:700 8.5px "Open Sans",sans-serif;color:#111;display:flex;align-items:center;gap:4px}
.more-link .dots{letter-spacing:1px;color:#777}

.projects{left:24px;top:801px;width:708px;height:155px;border-radius:10px;background:var(--row-pale);border:2px solid #d0d8cc}
.proj-table{position:absolute;left:10px;top:52px;width:686px;table-layout:fixed;border-collapse:separate;border-spacing:0 3px;font:700 8.5px "Open Sans",sans-serif}
.proj-table th{background:var(--green-deep);color:var(--white);font:700 10px "Open Sans",sans-serif;height:20px;text-align:left;padding-left:11px;white-space:nowrap}
.proj-table th:first-child{border-radius:10px 0 0 10px}
.proj-table th:last-child{border-radius:0 10px 10px 0}
.proj-table td{height:16px;padding-left:6px;border-left:2px solid var(--row-pale);white-space:nowrap}
.proj-table tr.alt td{background:var(--row-teal)}
.proj-table td:first-child{border-left:6px solid var(--row-pale)}
.proj-table td:last-child{border-right:6px solid var(--row-pale)}

.about{left:35px;top:972px;width:700px}
.about h2{font:400 11px "Open Sans",sans-serif;color:#111;border-bottom:1px dashed #aaa;padding-bottom:2px;width:655px}
.about h2 span{font-size:18px;color:var(--green)}
.about p{width:395px;font:400 10.5px/12px Arial,Helvetica,sans-serif;margin-top:14px}
.about .more-link{margin-top:16px}
.about-photo{left:430px;top:1003px;width:299px;height:130px;border-radius:8px;background:linear-gradient(180deg,#b7d66b,#6aa03a 45%,#2f5a1e)}

.site-footer{left:24px;top:1140px;width:708px;height:47px;border-radius:10px;background:linear-gradient(180deg,var(--forest-dark),var(--green-deep) 50%,var(--forest-dark));
  color:var(--white);font-size:8.5px;display:flex;align-items:center;justify-content:center;gap:8px}
</style>
</head>
<body>

<header class="abs site-header">
  <div class="abs util-bar">
    <span>Select Country</span>
    <select aria-label="Country"><option>Country</option></select>
    <span>Register</span><span class="sep">|</span><span>Log in</span>
  </div>
  <div class="abs brand"><span class="brand-dot"></span><span class="brand-name">TimberLinkup</span></div>
</header>

<section class="abs hero" role="img" aria-label="Photograph of a sunlit forest plantation with tall straight trunks"></section>
<h1 class="abs hero-title">Welcome to TimberLinkup</h1>

<nav class="abs main-nav">
  <a href="#">Post Projects</a><a href="#">Browse Projects</a><a href="#">About Us</a><a href="#">Contact</a>
</nav>

<div class="abs frame"></div>

<section class="abs featured">
  <h2>As Featured In</h2>
  <div class="partner-badges">
    <span class="badge wide"></span><span class="badge"></span><span class="badge"></span><span class="badge"></span><span class="badge"></span>
  </div>
</section>

<section class="abs how-it-works">
  <h2>How It Works</h2>
  <div class="steps">
    <div class="step"><div class="step-art" role="img" aria-label="Starburst new badge icon" style="background:#2a2a2a;border-radius:50%"></div><span class="step-label">Register</span></div>
    <div class="step"><div class="step-art" role="img" aria-label="Blue key button icon" style="background:radial-gradient(#7fb8f0,#1d56b5);border-radius:50%"></div><span class="step-label">Sign In</span></div>
    <div class="step"><div class="step-art" role="img" aria-label="Dark folder with green ruler icon" style="background:linear-gradient(#3a4a58,#1c2630)"></div><span class="step-label">Invite Project</span></div>
    <div class="step"><div class="step-art" role="img" aria-label="Orange folder with papers icon" style="background:linear-gradient(#ffd27a,#f08a12)"></div><span class="step-label">Selcet Project</span></div>
    <div class="step"><div class="step-art" role="img" aria-label="Group of users icon" style="background:linear-gradient(#f2b13a,#c0282a)"></div><span class="step-label">Complete Project</span></div>
  </div>
</section>

<section class="abs card signup">
  <div class="tab">Sign Up Now! <svg viewBox="0 0 12 12" fill="none" stroke="#fff" stroke-width="1.5"><path d="M5 2H2v8h8V7M7 1h4v4M11 1 5 7"/></svg></div>
  <h3 style="top:56px">Companies</h3>
  <ul style="top:72px">
    <li>Free 3 moths trial</li>
    <li>Post an expression of interest and receive applications</li>
    <li>Rate contractors after contract completion</li>
    <li>Find contractors and employees worldwide</li>
  </ul>
  <h3 style="top:146px">Contractors</h3>
  <ul style="top:162px">
    <li>Register and search for contractors</li>
    <li>Earn star ratings</li>
    <li>Receive automated emails for new expressions of interest</li>
    <li>3 month free trail then sign for optional 6 month / 1 year subscriptions</li>
    <li>Global connectivity or search locally</li>
  </ul>
</section>

<section class="abs card testimonial">
  <div class="tab">Testimonial <svg viewBox="0 0 12 12" fill="none" stroke="#fff" stroke-width="1.5"><path d="M5 2H2v8h8V7M7 1h4v4M11 1 5 7"/></svg></div>
  <div class="quote">
    <p><b>Lorem Ipsum</b> is simply dummy text of the printing and typesetting industry. Lorem Ipsum has been the industry's standard dummy text ever since the 1500s, when an unknown printer took a galley of type and scrambled it to make a type specimen book. It has survived not only five centuries, but also the leap into electronic typesetting, remaining essentially unchanged. It was popularised in the 1960s with the release of Typeset Co sheets containing Lorem Ipsum passages, and more recently with desktop publishing software like PageForm Desk including versions of Lorem Ipsum.</p>
    <p>It was popularised in the 1960s with the release of Typeset Co sheets containing Lorem Ipsum passages, and more recently with desktop publishing software like PageForm Desk including versions of Lorem Ipsum.</p>
  </div>
  <div class="byline">Posted By Tom Birch,CEO of Leafline Studio</div>
  <div class="abs more-link" style="left:212px;top:236px">More Testimonilas <span class="dots">····</span>›</div>
</section>

<section class="abs projects">
  <div class="tab">Recent Projects <svg viewBox="0 0 12 12" fill="none" stroke="#fff" stroke-width="1.5"><path d="M5 2H2v8h8V7M7 1h4v4M11 1 5 7"/></svg></div>
  <table class="proj-table">
    <colgroup><col style="width:156px"><col style="width:108px"><col style="width:64px"><col style="width:118px"><col style="width:84px"><col style="width:84px"><col style="width:72px"></colgroup>
    <thead><tr><th>Project Name</th><th>Employer</th><th>Tenders</th><th>Avg Tender Amount</th><th>Project Type</th><th>Posted Date</th><th>Time Left</th></tr></thead>
    <tbody>
      <tr class="alt"><td>Plantation new growth pruning</td><td>Ridgeway Forestry</td><td>6</td><td>$3000</td><td>Pruning</td><td>10/02/11</td><td>7 Days</td></tr>
      <tr><td>Seeding Transplanting</td><td>Fernvale Nurseries</td><td>15</td><td>$1000</td><td>Nursery</td><td>8/02/11</td><td>14 Days</td></tr>
      <tr class="alt"><td>Plantation new growth pruning</td><td>Ridgeway Forestry</td><td>6</td><td>$3000</td><td>Pruning</td><td>10/02/11</td><td>7 Days</td></tr>
    </tbody>
  </table>
</section>

<section class="abs about">
  <h2>what is <span>TimberLinkup.net?</span></h2>
  <p>TimberLinkup.net planns to connect people within the forestry industry, from employees to contractors aand professional worldwide.</p>
  <p>Currently our system hosts the most extensive database of its type anywhere, as our plans continue to expand our role in the world forestry industry is becoming widely recognised as an essential service.</p>
  <div class="more-link">More Information <span class="dots">····</span>›</div>
</section>
<div class="abs about-photo" role="img" aria-label="Photograph of a dirt path winding through a bright green forest"></div>

<footer class="abs site-footer">
  <span>© 2011, All Rights Reserved, TimberLinkup.net</span><span>|</span><span>Privacy Policy</span><span>|</span><span>Terms &amp; Conditions</span>
</footer>

</body>
</html>
```